Crestline Ridge Alloys Website

I need a redesign of my current website: www.crestlineridgealloys.example.
I would like to update the look, add some new stock photos of shiny stainless steel bar stock items. All of our grades of material should show on each page so that when people search for the grades on Google, our company site comes up. Most of the text content will be the same with some more changes. Also, we will want to add a button for calling our company for sales calls and one for sending a request for quote. I want the graphics to get prospects attention. I won't people to see us as a large stocking facility that is strong. Bold colors, silver, red, and blue.

Target Market(s)

Contract manufacturers, screw machine houses, medical instrument manufacturers, oil and gas parts industry, aerospace industry, automotive industry, food industry

Number of Pages Required

5+ page

Font styles to use
Sans Serif

Colors
ec1f27
0355a3

Requirements
Must have
• Pictures of stainless steel round bar. Also, a button linking someone to sales@crestlineridgealloys.example and our phone # 612-735-2048. Main stainless steel and titanium grades listed on each and every page. Also, a 1 page copy of our ISO 9001 certificatation.

```html
<!DOCTYPE html>
<html lang="en">
<head>
<meta charset="utf-8">
<title>Crestline Ridge Alloys</title>
<link rel="stylesheet" href="https://fonts.googleapis.com/css2?family=Open+Sans:wght@400;600;700&family=Oswald:wght@500&family=Montserrat:wght@400;700&display=swap">
<style>
:root{
  --red:#ec1f27;
  --blue:#0355a3;
  --blue-dark:#0a4a8f;
  --blue-light:#2e9ad6;
  --navy:#0d3f74;
  --grey-text:#8a8a8a;
  --hero-bg:#ededed;
  --footer:#181818;
  --white:#ffffff;
}
*{margin:0;padding:0;box-sizing:border-box}
html,body{width:1200px;height:900px;overflow:hidden;background:var(--white);font-family:"Open Sans",sans-serif}
.page{position:relative;width:1200px;height:900px;overflow:hidden}

.site-header{position:absolute;left:0;top:0;width:1200px;height:108px;background:linear-gradient(#f4f4f4,#ffffff)}
.brand{position:absolute;left:115px;top:20px;display:flex;align-items:center;gap:14px}
.brand-mark{width:50px;height:50px;background:var(--blue);border-radius:6px}
.brand-name{font-family:"Open Sans",sans-serif;font-weight:700;font-size:26px;line-height:29px;color:var(--red);width:230px}
.enquiry{position:absolute;left:633px;top:28px;display:flex;gap:8px}
.enquiry svg{margin-top:2px}
.enquiry-label{font-size:18px;color:#555;line-height:20px}
.enquiry-phone{font-size:23px;font-weight:700;color:var(--navy);line-height:28px}
.sales-btn{position:absolute;left:862px;top:32px;width:206px;height:38px;border-radius:3px;background:linear-gradient(#3c8bd0,#0e5aa8);box-shadow:0 1px 2px rgba(0,0,0,.3);color:var(--white);font-weight:600;font-size:19px;display:flex;align-items:center;padding-left:12px;gap:18px}

.main-nav{position:absolute;left:0;top:108px;width:1200px;height:46px;background:linear-gradient(#0b64b7,#06478e)}
.nav-list{position:absolute;left:104px;top:0;height:46px;display:flex;list-style:none}
.nav-list li{height:46px;display:flex;align-items:center;padding:0 17px;color:var(--white);font-size:14px;border-right:1px solid rgba(0,0,0,.18);box-shadow:1px 0 0 rgba(255,255,255,.1)}
.nav-list li.home{padding:0 18px 0 18px}
.nav-list li:last-child{border-right:none;box-shadow:none}
.search{position:absolute;left:891px;top:10px;width:189px;height:27px;background:var(--white);display:flex;align-items:center;justify-content:space-between;padding:0 6px 0 9px;font-size:13px;color:#999}

.hero{position:absolute;left:0;top:154px;width:1200px;height:344px;background:var(--hero-bg);overflow:hidden}
.hero-photo{position:absolute;left:420px;top:0;width:780px;height:344px;background:linear-gradient(135deg,#9aa3ab 0%,#5f6870 35%,#b8c0c7 55%,#4b535a 80%,#8c7a6e 100%);-webkit-mask-image:linear-gradient(90deg,transparent 0,#000 120px);mask-image:linear-gradient(90deg,transparent 0,#000 120px)}
.hero-copy{position:absolute;left:117px;top:84px;width:330px}
.hero-title{font-family:"Oswald",sans-serif;font-weight:500;font-size:31px;line-height:38px;letter-spacing:.3px;text-transform:uppercase}
.hero-title .accent{color:var(--red);display:block}
.hero-title .strong{color:var(--navy);display:block}
.hero-text{margin-top:8px;font-size:14.5px;line-height:23px;color:var(--grey-text)}
.read-more{margin-top:12px;display:flex;align-items:center;gap:10px;font-size:15px;color:var(--navy)}

.industries{position:absolute;left:117px;top:512px;display:flex;gap:8px}
.tile{position:relative;width:236px;height:300px;border-radius:0 34px 0 34px;overflow:hidden}
.tile-photo{position:absolute;inset:0}
.tile-panel{position:absolute;inset:0;clip-path:polygon(0 250px,236px 52px,236px 300px,0 300px)}
.tile.dark .tile-panel{background:var(--blue)}
.tile.light .tile-panel{background:var(--blue-light)}
.tile-badge{position:absolute;left:86px;top:101px;width:64px;height:64px;border-radius:50%;background:var(--white);display:flex;align-items:center;justify-content:center}
.tile-title{position:absolute;left:44px;top:227px;color:var(--white);font-family:"Montserrat",sans-serif;line-height:29px}
.tile-title b{display:block;font-weight:700;font-size:26px}
.tile-title span{display:block;font-weight:400;font-size:26px}

.site-footer{position:absolute;left:0;top:837px;width:1200px;height:63px;background:var(--footer)}
.copyright{position:absolute;left:129px;top:22px;font-size:13.5px;color:#d5d5d5}
.social{position:absolute;left:905px;top:16px;display:flex;gap:5px;list-style:none}
.social li{width:36px;height:32px;background:var(--blue)}
.social li:nth-child(2){background:var(--blue-light)}
.social li:nth-child(3){background:var(--red)}
</style>
</head>
<body>
<div class="page">
  <header class="site-header">
    <div class="brand">
      <div class="brand-mark"></div>
      <div class="brand-name">Crestline Ridge Alloys</div>
    </div>
    <div class="enquiry">
      <svg width="44" height="44" viewBox="0 0 44 44" aria-hidden="true">
        <circle cx="22" cy="22" r="20" fill="none" stroke="#0d3f74" stroke-width="2"/>
        <path d="M17 11c-2 1-4 3-3 8 1 6 5 12 10 14 3 1 5 0 6-2l-3-4-3 2c-2-1-4-5-5-8l3-2-2-5z" fill="#0d3f74"/>
      </svg>
      <div>
        <div class="enquiry-label">For Enquiries, Call</div>
        <div class="enquiry-phone">011 555 0193</div>
      </div>
    </div>
    <div class="sales-btn">
      <svg width="22" height="26" viewBox="0 0 22 26" aria-hidden="true">
        <rect x="2" y="3" width="18" height="22" rx="2" fill="none" stroke="#fff" stroke-width="2"/>
        <rect x="7" y="1" width="8" height="5" rx="1" fill="#fff"/>
        <path d="M6 15l4 4 7-8" fill="none" stroke="#fff" stroke-width="2.4"/>
      </svg>
      Sales Enquiry
    </div>
  </header>

  <nav class="main-nav">
    <ul class="nav-list">
      <li class="home"><svg width="22" height="18" viewBox="0 0 22 18" aria-label="Home"><path d="M11 1L1 10h3v7h5v-5h4v5h5v-7h3z" fill="#fff"/></svg></li>
      <li>Products</li>
      <li>Quality</li>
      <li>Locations</li>
      <li>Hard To Find Services</li>
      <li>Large Volume</li>
      <li>Inquiries</li>
      <li>Faq</li>
    </ul>
    <div class="search">Search
      <svg width="17" height="17" viewBox="0 0 17 17" aria-hidden="true"><circle cx="7" cy="7" r="5.5" fill="none" stroke="#222" stroke-width="2.2"/><path d="M11 11l5 5" stroke="#222" stroke-width="2.6"/></svg>
    </div>
  </nav>

  <section class="hero">
    <div class="hero-photo" role="img" aria-label="Stacked stainless steel square tubing"></div>
    <div class="hero-copy">
      <h1 class="hero-title"><span class="accent">Welcome to Crestline</span><span class="strong">Ridge Alloys</span></h1>
      <p class="hero-text">Lorem Ipsum is simply dummy text of the printing and typesetting industry. Lorem Ipsum has been the industry's standard dummy text ever</p>
      <div class="read-more"><svg width="8" height="10" viewBox="0 0 8 10" aria-hidden="true"><path d="M1 1l5 4-5 4" fill="none" stroke="#0d3f74" stroke-width="2"/></svg>Read More</div>
    </div>
  </section>

  <section class="industries">
    <div class="tile dark">
      <div class="tile-photo" role="img" aria-label="Oil pump jack under a blue sky" style="background:linear-gradient(160deg,#6f9fd8,#b9cfe6 60%,#8b8f7a)"></div>
      <div class="tile-panel"></div>
      <div class="tile-badge"><svg width="34" height="36" viewBox="0 0 34 36" aria-hidden="true"><path d="M17 2L7 32M17 2l10 30M11 20h12M9 26h16M3 33h28" stroke="#0355a3" stroke-width="3" fill="none"/></svg></div>
      <div class="tile-title"><b>Oil &amp; Gas</b><span>Industry »</span></div>
    </div>
    <div class="tile light">
      <div class="tile-photo" role="img" aria-label="Car assembly line" style="background:linear-gradient(160deg,#c9ccd0,#7f868d 50%,#b5b9bd)"></div>
      <div class="tile-panel"></div>
      <div class="tile-badge"><svg width="32" height="34" viewBox="0 0 32 34" aria-hidden="true"><rect x="4" y="3" width="16" height="28" rx="2" fill="#2e9ad6"/><rect x="7" y="6" width="10" height="8" fill="#fff"/><path d="M20 10h5v16a3 3 0 0 0 5 0V12" fill="none" stroke="#2e9ad6" stroke-width="2.5"/></svg></div>
      <div class="tile-title"><b>Automoitve</b><span>Industry »</span></div>
    </div>
    <div class="tile dark">
      <div class="tile-photo" role="img" aria-label="Stainless steel medical tubing and fittings" style="background:linear-gradient(160deg,#e2e4e6,#9ea3a8 50%,#c7cacd)"></div>
      <div class="tile-panel"></div>
      <div class="tile-badge"><svg width="30" height="30" viewBox="0 0 30 30" aria-hidden="true"><path d="M11 2h8v9h9v8h-9v9h-8v-9H2v-8h9z" fill="#0355a3"/></svg></div>
      <div class="tile-title"><b>Medical</b><span>Instrument »</span></div>
    </div>
    <div class="tile light">
      <div class="tile-photo" role="img" aria-label="Jet aircraft over a carrier deck at sunset" style="background:linear-gradient(170deg,#f0c27a,#d98a4a 45%,#5a5650)"></div>
      <div class="tile-panel"></div>
      <div class="tile-badge"><svg width="36" height="36" viewBox="0 0 36 36" aria-hidden="true"><path d="M18 2c2 0 2.5 3 2.5 6v6l13 7v3l-13-3v7l4 3v2l-6.5-1.5L11.5 33v-2l4-3v-7l-13 3v-3l13-7V8c0-3 .5-6 2.5-6z" fill="#2e9ad6"/></svg></div>
      <div class="tile-title"><b>Aerospace</b><span>Industry »</span></div>
    </div>
  </section>

  <footer class="site-footer">
    <p class="copyright">Content copyright 2009-2014. Crestline Ridge Alloys, Inc</p>
    <ul class="social" aria-label="Social links">
      <li></li><li></li><li></li><li></li>
    </ul>
  </footer>
</div>
</body>
</html>
```